Business Card Design

Electronic Security
Alarm Systems
CCTV
Electronic Access Control
Security System Integration

Industry/Entity Type

Business

Contact Information for Business Card

Declan Whitfield
PO Box 862
Carrowbrook Qld 4179
Phone 07 38265014
Mob 0428615937

```html
<!DOCTYPE html>
<html lang="en">
<head>
<meta charset="utf-8">
<title>Ardent Security Group – Business Card</title>
<link rel="stylesheet" href="https://fonts.googleapis.com/css2?family=Arimo:wght@400;700&display=swap">
<style>
  :root {
    --page-bg: #ececec;
    --card-white: #ffffff;
    --card-black: #000000;
    --text-light: #ffffff;
    --accent-yellow: #f7c20a;
    --brand-blue: #2b95d1;
  }
  * { box-sizing: border-box; margin: 0; padding: 0; }
  html, body {
    width: 1200px;
    height: 864px;
    overflow: hidden;
    background: var(--page-bg);
    font-family: "Arimo", Arial, sans-serif;
  }
  .canvas {
    position: relative;
    width: 1200px;
    height: 864px;
  }
  .business-card {
    position: absolute;
    left: 150px;
    top: 157px;
    width: 900px;
    height: 550px;
    background: var(--card-white);
    overflow: hidden;
    box-shadow: 0 10px 30px rgba(0,0,0,0.12);
  }
  .contact-panel {
    position: absolute;
    left: 405px;
    top: 32px;
    right: 0;
    bottom: 0;
    background: var(--card-black);
  }
  .bottom-band {
    position: absolute;
    left: 0;
    right: 0;
    bottom: 0;
    height: 50px;
    background: var(--card-black);
  }
  .brand {
    position: absolute;
    left: 0;
    top: 32px;
    width: 405px;
    height: 468px;
    display: flex;
    align-items: center;
    justify-content: center;
    gap: 14px;
  }
  .brand-mark {
    width: 26px;
    height: 26px;
    background: var(--brand-blue);
  }
  .brand-name {
    font-weight: 700;
    font-size: 30px;
    letter-spacing: 1px;
    color: var(--brand-blue);
  }
  .holder-name {
    position: absolute;
    left: 60px;
    top: 84px;
    font-weight: 700;
    font-size: 40px;
    color: var(--text-light);
    word-spacing: 10px;
  }
  .contact-list {
    position: absolute;
    left: 60px;
    top: 212px;
    list-style: none;
    color: var(--text-light);
    font-size: 22px;
    line-height: 1.2;
  }
  .contact-item {
    display: flex;
    align-items: flex-start;
    margin-bottom: 24px;
  }
  .contact-icon {
    width: 22px;
    height: 22px;
    margin-right: 50px;
    margin-top: 2px;
    fill: var(--accent-yellow);
    flex: none;
  }
</style>
</head>
<body>
<div class="canvas">
  <div class="business-card">
    <div class="brand">
      <span class="brand-mark"></span>
      <span class="brand-name">ARDENT</span>
    </div>

    <div class="contact-panel">
      <h1 class="holder-name">Declan Whitfield</h1>
      <ul class="contact-list">
        <li class="contact-item">
          <svg class="contact-icon" viewBox="0 0 24 24" aria-hidden="true">
            <path d="M3 7c0-2 4-4 9-4s9 2 9 4v2h-5V7H8v2H3z"/>
            <path d="M6 10h12l2 10H4z"/>
            <circle cx="12" cy="15" r="2.5" fill="#000"/>
          </svg>
          <span>07 38265014</span>
        </li>
        <li class="contact-item">
          <svg class="contact-icon" viewBox="0 0 24 24" aria-hidden="true">
            <rect x="7" y="2" width="10" height="20" rx="2"/>
            <rect x="9" y="5" width="6" height="5" fill="#000"/>
            <rect x="9" y="12" width="2" height="2" fill="#000"/>
            <rect x="13" y="12" width="2" height="2" fill="#000"/>
            <rect x="9" y="16" width="2" height="2" fill="#000"/>
            <rect x="13" y="16" width="2" height="2" fill="#000"/>
          </svg>
          <span>0428615937</span>
        </li>
        <li class="contact-item">
          <svg class="contact-icon" viewBox="0 0 24 24" aria-hidden="true">
            <path d="M12 2 2 11h3v10h5v-6h4v6h5V11h3z"/>
          </svg>
          <span>PO Box 862 Carrowbrook<br>Qld 4179</span>
        </li>
      </ul>
    </div>

    <div class="bottom-band"></div>
  </div>
</div>
</body>
</html>
```